Graphic background for 10 Pull Up Banners

To produce a graphic background for a 100 cm wide by 200 cm high Pull-Up Display banner containing a Buddhist text in three languages: Tibetan, Mandarin and English. Please refer to uploaded file "Elements of Pull Up Banner". The design should be simple (not drawing attention away from the text). This design should then be varied for or extended to the next banner and so on until the 10th banner. When the banners are lined up, they should form a single design that is 1000 cm wide by 200 cm high.
An alternative way to look at the project is to produce a graphic background of 1000 cm width by 200 cm height that is then splitted into ten separate 100 cm wide by 200 cm high graphic to be used as background for 10 Buddhist texts (text 1, 2, 3, 4, 5, 6, 7, 8, 9a, 9b) on 10 Pull-Up Display Banners, the text in each banner being in the three languages mentioned earlier.
In either perspective, the design should be simple and not draw attention away from the texts. See uploaded PDF file "Examples.pdf"
For attendees at a Buddhist Event.

```html
<!DOCTYPE html>
<html lang="en">
<head>
<meta charset="utf-8">
<title>Pull-Up Banners — Ten Mistaking / Desire &amp; Attachment</title>
<link href="https://fonts.googleapis.com/css2?family=Cabin:wght@400;500&family=Noto+Sans+SC:wght@300&family=Noto+Serif+SC:wght@400&family=Noto+Serif+Tibetan:wght@400&display=swap" rel="stylesheet">
<style>
  :root {
    --page: #ecebe8;
    --aqua: #bfe9ec;
    --aqua-soft: #e4f6f6;
    --white: #ffffff;
    --ink: #1d1d1f;
    --ink-soft: #33383a;
    --orange: #f2a446;
    --deity-red: #d9606a;
    --deity-pale: #f6dadd;
  }
  * { box-sizing: border-box; margin: 0; padding: 0; }
  html, body { width: 1200px; height: 960px; overflow: hidden; background: var(--page); }
  .stage { position: relative; width: 1200px; height: 960px; }

  .banner {
    position: absolute; top: 97px; width: 406px; height: 812px; overflow: hidden;
    background:
      radial-gradient(circle at 78% 48%, rgba(255,255,255,.55) 0 70px, transparent 71px),
      radial-gradient(circle at 20% 82%, rgba(255,255,255,.35) 0 90px, transparent 91px),
      radial-gradient(ellipse at 70% 40%, var(--aqua) 0%, transparent 60%),
      radial-gradient(ellipse at 15% 60%, var(--aqua) 0%, transparent 55%),
      linear-gradient(180deg, var(--white) 0%, var(--aqua-soft) 35%, #d4f0f1 60%, var(--aqua-soft) 100%);
    box-shadow: 0 6px 18px rgba(0,0,0,.25);
  }
  .banner--mistaking { left: 162px; }
  .banner--desire { left: 612px; }

  .halo {
    position: absolute; width: 258px; height: 258px; border-radius: 50%;
    background: var(--white);
    border-bottom: 3px solid var(--orange);
    border-left: 2px solid var(--orange);
    border-right: 2px solid var(--orange);
    border-top: 0;
  }
  .banner--mistaking .halo { left: 73px; top: -45px; }
  .banner--desire .halo { left: 76px; top: -37px; }

  .deity {
    position: absolute; width: 142px; height: 166px; border-radius: 40% 40% 6px 6px;
    background: radial-gradient(ellipse at 50% 45%, var(--deity-pale), #fbeeee 70%);
    border: 1px solid var(--deity-red);
  }
  .banner--mistaking .deity { left: 131px; top: 24px; }
  .banner--desire .deity { left: 134px; top: 26px; }

  .title-zh {
    position: absolute; left: 0; width: 100%; text-align: center;
    font-family: "Noto Sans SC", sans-serif; font-weight: 300; color: var(--ink);
  }
  .title-en {
    position: absolute; left: 0; width: 100%; text-align: center;
    font-family: "Cabin", sans-serif; font-weight: 500; color: var(--ink);
  }
  .banner--mistaking .title-zh { top: 240px; font-size: 32px; letter-spacing: 2px; }
  .banner--mistaking .title-en { top: 282px; font-size: 31px; }
  .banner--desire .title-zh { top: 230px; font-size: 33px; letter-spacing: 2px; }
  .banner--desire .title-en { top: 274px; font-size: 31px; }

  .verses-en {
    position: absolute; left: 34px; right: 34px; list-style: none; text-align: center;
    font-family: "Cabin", sans-serif; color: var(--ink);
  }
  .banner--mistaking .verses-en { top: 340px; font-size: 8.3px; line-height: 10px; }
  .banner--mistaking .verses-en li { margin-bottom: 9px; }
  .banner--desire .verses-en { top: 350px; font-size: 11.5px; line-height: 14px; left: 20px; right: 20px; }
  .banner--desire .verses-en li { margin-bottom: 11px; }

  .notes { position: absolute; top: 578px; left: 28px; right: 14px; display: flex; gap: 18px; }
  .notes-bo {
    list-style: none; width: 160px;
    font-family: "Noto Serif Tibetan", serif; font-size: 6.5px; line-height: 15.8px; color: var(--ink-soft);
    white-space: nowrap;
  }
  .notes-zh {
    list-style: none; font-family: "Noto Serif SC", serif; font-size: 8px; line-height: 11.8px; color: var(--ink-soft);
  }
  .notes-zh .footnotes { margin-top: 9px; }

  .verses-bo {
    position: absolute; top: 478px; left: 0; width: 100%; list-style: none; text-align: center;
    font-family: "Noto Serif Tibetan", serif; font-size: 16px; line-height: 30.5px; color: var(--ink);
  }
  .verses-zh {
    position: absolute; top: 632px; left: 101px; list-style: none;
    font-family: "Noto Serif SC", serif; font-size: 21px; line-height: 28px; letter-spacing: 3px; color: var(--ink-soft);
  }
</style>
</head>
<body>
<main class="stage">

  <section class="banner banner--mistaking">
    <div class="halo"></div>
    <div class="deity" role="img" aria-label="Red line illustration of a seated deity on a lotus throne"></div>
    <h2 class="title-zh">十个误解</h2>
    <h1 class="title-en">Ten Mistaking</h1>
    <ul class="verses-en">
      <li>Desire can be mistaken for faith or devotion.</li>
      <li>Attachment can be mistaken for love and compassion.</li>
      <li>Conceptual emptiness can be mistaken for the emptiness of the nature of phenomena.</li>
      <li>Nihilism can be mistaken for the dharmadhatu.</li>
      <li>A meditative experience can be mistaken for realization.</li>
      <li>Outer religious practices can be mistaken for inner development of good qualities.</li>
      <li>A person in the grip of a demon can be mistaken for a person who has destroyed his own delusions.</li>
      <li>A charlatan can be mistaken for a siddha.</li>
      <li>An act to benefit yourself can be mistaken for an act to benefit others.</li>
      <li>Deviousness can be mistaken for skilful means.</li>
    </ul>
    <div class="notes">
      <ul class="notes-bo" lang="bo">
        <li>དད་པ་དང་འདོད་པ་འཁྲུལ་སྲིད།</li>
        <li>བྱམས་སྙིང་རྗེ་དང་ཆགས་པ་འཁྲུལ་སྲིད།</li>
        <li>ཤེས་བྱ་སྟོང་པ་དང་བློ་སྟོང་འཁྲུལ་སྲིད།</li>
        <li>ཆོས་དབྱིངས་དང་ཆད་ལྟ་འཁྲུལ་སྲིད།</li>
        <li>ཉམས་དང་རྟོགས་པ་འཁྲུལ་སྲིད།</li>
        <li>བརྟུལ་ཞུགས་དང་སྒྲུབ་པ་འཁྲུལ་སྲིད།</li>
        <li>འདྲེ་དང་གྲུབ་ཐོབ་འཁྲུལ་སྲིད།</li>
        <li>གྲུབ་ཐོབ་དང་ཆོམ་རྐུན་འཁྲུལ་སྲིད།</li>
        <li>གཞན་དོན་དང་རང་དོན་འཁྲུལ་སྲིད།</li>
        <li>ཐབས་མཁས་དང་གཡོ་སྒྱུ་འཁྲུལ་སྲིད།</li>
      </ul>
      <ul class="notes-zh" lang="zh">
        <li>信心与爱欲可能混淆，</li>
        <li>慈悲与贪执可能混淆，</li>
        <li>所知¹本空与思维造作空性可能混淆，</li>
        <li>法界与断见²可能混淆，</li>
        <li>觉受与证悟可能混淆，</li>
        <li>尊者与神棍可能混淆，</li>
        <li>破惑与着魔可能混淆，</li>
        <li>成就者与骗子可能混淆，</li>
        <li>利他与自利可能混淆，</li>
        <li>方便善巧与谄媚哄骗可能混淆。</li>
        <li class="footnotes">1. 所知：可以认识的外境。</li>
        <li>2. 断见：否定因果、前生、后世等说法的见解。</li>
      </ul>
    </div>
  </section>

  <section class="banner banner--desire">
    <div class="halo"></div>
    <div class="deity" role="img" aria-label="Red line illustration of a seated deity on a lotus throne"></div>
    <h2 class="title-zh">欲与爱</h2>
    <h1 class="title-en">Desire &amp; Attachment</h1>
    <ul class="verses-en">
      <li>If you have no desire, your goal cannot be achieved.</li>
      <li>Since not all desire is attachment,</li>
      <li>not knowing how to differentiate desire from attachment,</li>
      <li>to talk about bringing passion into the path is absurd.</li>
    </ul>
    <ul class="verses-bo" lang="bo">
      <li>འདོད་པ་མེད་ན་རང་དོན་མི་འགྲུབ་ཀྱང་།</li>
      <li>འདོད་པ་ཡོད་ཚད་ཆགས་པ་མི་ཡིན་པས།</li>
      <li>འདོད་དང་ཆགས་པའི་ཁྱད་པར་མ་ཤེས་པར།</li>
      <li>འདོད་ཆགས་ལམ་དུ་སློང་བར་སྨྲ་བ་རེས།</li>
    </ul>
    <ul class="verses-zh" lang="zh">
      <li>若无意欲则不成自利，</li>
      <li>然有意欲非为执着故，</li>
      <li>不知意欲执着差别即，</li>
      <li>贪执说所当取确荒唐。</li>
    </ul>
  </section>

</main>
</body>
</html>
```